Brass Kettle Business Card

I needed some business cards done for my band. We are a 9 piece funk/horn band that plays a lot of private parties, wedding receptions and music festivals. We'd like a design with vivid colors that incorporates our logo. You can check out our website at www.brasskettleband.com to see what type of vibe we are going for.

```html
<!DOCTYPE html>
<html lang="en">
<head>
<meta charset="utf-8">
<title>Brass Kettle Business Card</title>
<link href="https://fonts.googleapis.com/css2?family=Poppins:wght@400;700&family=Great+Vibes&display=swap" rel="stylesheet">
<style>
  :root {
    --page: #d6d6d6;
    --card: #161616;
    --lime: #c8dc26;
    --ink: #f2f2f2;
    --rule: #3a3a3a;
  }
  * { box-sizing: border-box; margin: 0; padding: 0; }
  html, body { width: 1200px; height: 800px; overflow: hidden; }
  body {
    background: var(--page);
    font-family: "Poppins", sans-serif;
    display: flex;
    align-items: center;
    justify-content: center;
    gap: 40px;
  }
  .card {
    width: 540px;
    height: 309px;
    background: var(--card);
    border-bottom: 3px solid var(--lime);
    border-left: 2px solid var(--lime);
    position: relative;
    display: flex;
  }
  .brand-name {
    font-family: "Poppins", sans-serif;
    font-weight: 700;
    color: var(--lime);
    white-space: nowrap;
  }
  .card-back .brand-side {
    width: 47%;
    display: flex;
    align-items: center;
    justify-content: center;
  }
  .card-back .brand-name { font-size: 30px; }
  .divider {
    position: absolute;
    left: 47%;
    top: 0;
    width: 1px;
    height: 52%;
    background: linear-gradient(var(--rule), #5a5a5a, transparent);
  }
  .contact-side {
    width: 53%;
    padding: 34px 24px 0 22px;
    color: var(--ink);
  }
  .person-name {
    font-family: "Great Vibes", cursive;
    color: var(--lime);
    font-size: 36px;
    line-height: 1;
  }
  .person-role { font-size: 13px; margin: 2px 0 14px; }
  .contact-list { list-style: none; font-size: 12.5px; line-height: 1.6; }
  .contact-list li { display: flex; align-items: center; gap: 8px; }
  .contact-list svg { width: 13px; height: 13px; flex: none; }
  .accent { color: var(--lime); }
  .address { font-size: 12.5px; line-height: 1.45; margin-top: 12px; }
  .card-front { align-items: center; justify-content: center; }
  .card-front .brand-name { font-size: 56px; }
</style>
</head>
<body>
  <section class="card card-back">
    <div class="brand-side">
      <span class="brand-name">Brass Kettle</span>
    </div>
    <span class="divider"></span>
    <div class="contact-side">
      <h1 class="person-name">Marcus Delaney</h1>
      <p class="person-role">Managing Director</p>
      <ul class="contact-list">
        <li>
          <svg viewBox="0 0 16 16" aria-hidden="true"><path d="M3 1.5l3 3-1.6 1.8a9 9 0 0 0 5.3 5.3L11.5 10l3 3-2 2C6.5 15 1 9.5 1 3.5z" fill="var(--lime)"/></svg>
          044-555 018 274
        </li>
        <li>
          <svg viewBox="0 0 16 16" aria-hidden="true"><rect x="1" y="3" width="14" height="10" fill="var(--lime)"/><path d="M1 3l7 6 7-6" fill="none" stroke="var(--card)" stroke-width="1.4"/></svg>
          info@brasskettle.com
        </li>
        <li>
          <svg viewBox="0 0 16 16" aria-hidden="true"><circle cx="8" cy="8" r="7" fill="var(--lime)"/><g fill="none" stroke="var(--card)" stroke-width="1"><ellipse cx="8" cy="8" rx="3" ry="7"/><path d="M1 8h14M2.5 4.5h11M2.5 11.5h11"/></g></svg>
          <span>www.<span class="accent">brasskettleband</span>.com</span>
        </li>
      </ul>
      <p class="address">421, Address line goes here<br>45452,Country Name</p>
    </div>
  </section>
  <section class="card card-front">
    <span class="brand-name">Brass Kettle</span>
  </section>
</body>
</html>
```